NEW Brand "New Zealand Wine Estate"

We are looking for a design for our new range of New Zealand wine. An estate label that can be used for several varietals.
We have three potential names...
Hollow Pine Estate
Velvet Morrow Estate
Tovrina Estate
first variant is "Central Otago Pinot Noir" please use this in the original design.
This brand is for world export, so will need to be appealing to many markets but representative of New Zealand and our rugged Coasts.
Target Market(s)
Supermarket $25 NZD per bottle price point. Young and hip
Font styles to use
Decorative
Script
Requirements
Must have
- Sophistication but edgy. Stand out on a shelf.
- the brand needs to be able to be used for red or white wine.

```html
<!DOCTYPE html>
<html lang="en">
<head>
<meta charset="utf-8">
<title>Tovrina Estate – Central Otago Pinot Noir Label</title>
<link rel="stylesheet" href="https://fonts.googleapis.com/css2?family=Kaushan+Script&family=Cinzel:wght@500;700&family=Montserrat:wght@500;600&display=swap">
<style>
  :root {
    --page: #f3f3f1;
    --label-navy: #1d2a35;
    --label-navy-deep: #141d25;
    --gold: #b39a66;
    --cream: #e9dcc0;
    --vintage-rule: #8e3a2c;
    --ink-light: #d9d3c4;
    --ship-tone-a: #3a4a57;
    --ship-tone-b: #24323e;
  }
  * { margin: 0; padding: 0; box-sizing: border-box; }
  html, body {
    width: 1200px;
    height: 2808px;
    overflow: hidden;
    background: var(--page);
  }
  .canvas {
    position: relative;
    width: 1200px;
    height: 2808px;
  }
  .wine-label {
    position: absolute;
    left: 180px;
    top: 154px;
    width: 840px;
    height: 2500px;
  }
  .label-motto {
    font-family: "Montserrat", sans-serif;
    font-weight: 600;
    font-size: 25px;
    letter-spacing: 2.5px;
    fill: var(--ink-light);
  }
  .brand-name {
    font-family: "Kaushan Script", cursive;
    fill: var(--cream);
  }
  .vintage {
    font-family: "Montserrat", sans-serif;
    font-weight: 500;
    font-size: 58px;
    letter-spacing: 8px;
    fill: var(--vintage-rule);
  }
  .spec {
    font-family: "Montserrat", sans-serif;
    font-weight: 500;
    font-size: 52px;
    letter-spacing: 3px;
    fill: var(--ink-light);
  }
  .region {
    font-family: "Montserrat", sans-serif;
    font-weight: 600;
    font-size: 40px;
    letter-spacing: 6px;
    fill: var(--ink-light);
  }
  .varietal {
    font-family: "Cinzel", serif;
    font-weight: 700;
    font-size: 84px;
    letter-spacing: 4px;
    fill: var(--cream);
  }
</style>
</head>
<body>
<main class="canvas">
  <svg class="wine-label" viewBox="0 0 840 2500" xmlns="http://www.w3.org/2000/svg" aria-label="Tovrina Estate Central Otago Pinot Noir wine label">
    <defs>
      <linearGradient id="labelFill" x1="0" y1="0" x2="1" y2="0">
        <stop offset="0" stop-color="var(--label-navy-deep)"/>
        <stop offset="0.5" stop-color="var(--label-navy)"/>
        <stop offset="1" stop-color="var(--label-navy-deep)"/>
      </linearGradient>
      <linearGradient id="shipFill" x1="0" y1="0" x2="0" y2="1">
        <stop offset="0" stop-color="var(--ship-tone-a)"/>
        <stop offset="1" stop-color="var(--ship-tone-b)"/>
      </linearGradient>
      <path id="mottoArc" d="M120,430 A300,300 0 0 1 720,430"/>
    </defs>

    <!-- label body with gold frame -->
    <path class="label-body" d="M0,420 A420,420 0 0 1 840,420 V2080 A420,420 0 0 1 0,2080 Z" fill="url(#labelFill)"/>
    <path class="label-frame" d="M22,420 A398,398 0 0 1 818,420 V2080 A398,398 0 0 1 22,2080 Z" fill="none" stroke="var(--gold)" stroke-width="6"/>

    <!-- arched motto -->
    <text class="label-motto">
      <textPath href="#mottoArc" startOffset="50%" text-anchor="middle">CLASSIC, PASSIONATE &amp; UNIQUELY NEW ZEALAND WINE</textPath>
    </text>

    <!-- sailing ship illustration area -->
    <rect class="ship-illustration" x="240" y="250" width="360" height="500" rx="40" fill="url(#shipFill)" role="img" aria-label="Engraved illustration of a sailing ship on rough waves"/>

    <!-- brand name -->
    <text class="brand-name" x="420" y="1010" text-anchor="middle" font-size="210">Tovrina</text>
    <text class="brand-name" x="420" y="1200" text-anchor="middle" font-size="150">Estate</text>

    <!-- vintage with rules -->
    <line x1="190" y1="1478" x2="310" y2="1478" stroke="var(--vintage-rule)" stroke-width="4"/>
    <text class="vintage" x="424" y="1500" text-anchor="middle">2016</text>
    <line x1="530" y1="1478" x2="650" y2="1478" stroke="var(--vintage-rule)" stroke-width="4"/>

    <!-- specs -->
    <text class="spec" x="420" y="1800" text-anchor="middle">18%</text>
    <text class="spec" x="420" y="1870" text-anchor="middle">75 cl.</text>
    <text class="region" x="420" y="1990" text-anchor="middle">CENTRAL OTAGO</text>
    <text class="varietal" x="420" y="2090" text-anchor="middle">PINOT NOIR</text>
  </svg>
</main>
</body>
</html>
```